Compass of Quiet Mornings book cover design

Book cover - the book contains 52 chapters - 2 for each letter of the alphabet, so a yearlong focus on Leadership. The Intent is to communicate that leadership is common sense. It just isn’t common practice. This book allows the reader to focus on one leadership word each week for a yearlong focus on improving one’s leadership. It is full of stories relating to the 52 words that will challenge and inspire the reader.
Target Market(s)
Leaders / Emerging Leaders
Industry/Entity Type
All
Requirements
Must have
- Appeal to executives
Nice to have
- Simplicity
Should not have
- Cartoon feel

```html
<!DOCTYPE html>
<html lang="en">
<head>
<meta charset="utf-8">
<title>Compass of Quiet Mornings – Book Cover</title>
<link rel="stylesheet" href="https://fonts.googleapis.com/css2?family=Barlow+Condensed:wght@700&family=Plus+Jakarta+Sans:wght@300;700&display=swap">
<style>
  :root {
    --backdrop: #9e9e9e;
    --paper: #ffffff;
    --accent-red: #d0403a;
    --ink: #1b1a17;
    --rule: #1b1a17;
    --mist-deep: #c3ceda;
    --mist-mid: #d9e1e8;
    --mist-pale: #edf1f3;
  }
  html, body {
    margin: 0;
    padding: 0;
    width: 1200px;
    height: 1200px;
    overflow: hidden;
    background: var(--backdrop);
  }
  .book-cover {
    position: absolute;
    left: 251px;
    top: 74px;
    width: 705px;
    height: 1059px;
    background: var(--paper);
    overflow: hidden;
  }
  .cover-illustration {
    position: absolute;
    left: 8px;
    top: 92px;
    width: 690px;
    height: 384px;
    border-radius: 4px;
    background: linear-gradient(180deg,
      var(--mist-pale) 0%,
      var(--mist-mid) 30%,
      var(--mist-deep) 62%,
      var(--mist-mid) 84%,
      var(--paper) 100%);
  }
  .title-art {
    position: absolute;
    left: 0;
    top: 0;
    width: 705px;
    height: 900px;
  }
  .title-line {
    font-family: "Barlow Condensed", "Arial Narrow", sans-serif;
    font-weight: 700;
  }
  .title-top { fill: var(--accent-red); font-size: 143px; }
  .title-middle { fill: var(--accent-red); font-size: 44px; }
  .title-bottom { fill: var(--ink); font-size: 246px; }
  .title-rule { stroke: var(--rule); stroke-width: 1.5; }
  .subtitle {
    position: absolute;
    left: 0;
    width: 705px;
    top: 878px;
    margin: 0;
    text-align: center;
    font-family: "Plus Jakarta Sans", "Helvetica Neue", sans-serif;
    font-weight: 300;
    font-size: 22px;
    line-height: 30px;
    letter-spacing: -0.4px;
    color: var(--ink);
  }
  .author-name {
    position: absolute;
    left: 0;
    width: 705px;
    top: 984px;
    margin: 0;
    text-align: center;
    font-family: "Plus Jakarta Sans", "Helvetica Neue", sans-serif;
    font-weight: 700;
    font-size: 45px;
    line-height: 50px;
    letter-spacing: -1.8px;
    color: var(--accent-red);
  }
</style>
</head>
<body>
  <main class="book-cover">
    <div class="cover-illustration" role="img" aria-label="Line-drawn snowy mountain range with a red route of lettered markers A to Z climbing to a flag on the summit"></div>

    <svg class="title-art" viewBox="0 0 705 900" aria-labelledby="cover-title">
      <title id="cover-title">Compass of Quiet Mornings</title>
      <text class="title-line title-top" x="65" y="586" textLength="579" lengthAdjust="spacingAndGlyphs">COMPASS</text>
      <line class="title-rule" x1="63" y1="615" x2="278" y2="615"/>
      <text class="title-line title-middle" x="290" y="633" textLength="126" lengthAdjust="spacingAndGlyphs">OF QUIET</text>
      <line class="title-rule" x1="428" y1="615" x2="643" y2="615"/>
      <text class="title-line title-bottom" x="66" y="820" textLength="581" lengthAdjust="spacingAndGlyphs">MORNINGS</text>
    </svg>

    <p class="subtitle">Focus on One Leadership Word Each Week For a Year<br>Long Focus on Improving One’s Leadership.</p>
    <p class="author-name">AUTHOR NAME HERE</p>
  </main>
</body>
</html>
```